Floristry Business Card Design Project

I have a logo now and am looking to incorporate this into a business card. I would like a double sided business card. I would like one side to be decorative so that it blends well when included with floral arrangements and that can also be used as the front of a card and the other side will contain the business details. The font on the business details side should be clear although some decorative font would be ok. I have included the logo files for use in the business card design.

Feel free to break up the logo and use certain aspects of it in the design. Really looking for something that stands out and that is really creative.

Industry/Entity Type

Floral

Requirements
Should not have
• Nothing tacky or corny. The logo should be clearly read (perhaps a background colour).

```html
<!DOCTYPE html>
<html lang="en">
<head>
<meta charset="utf-8">
<title>Petal Hollow – Business Card</title>
<link rel="stylesheet" href="https://fonts.googleapis.com/css2?family=Open+Sans:wght@400;600&display=swap">
<style>
  :root {
    --backdrop: #ececec;
    --salmon: #e09b81;
    --card-white: #ffffff;
    --mint: #7fc3a2;
    --ink: #444444;
    --rule: #c9c9c9;
    --accent: #e59a79;
  }
  * { box-sizing: border-box; margin: 0; padding: 0; }
  html, body {
    width: 1200px; height: 974px; overflow: hidden;
    background: var(--backdrop);
    font-family: "Open Sans", Arial, sans-serif;
  }
  .sheet {
    position: relative; width: 1200px; height: 974px;
    display: flex; flex-direction: column; align-items: center; justify-content: center; gap: 60px;
  }
  .card {
    position: relative; width: 700px; height: 400px; border-radius: 30px;
    box-shadow: 0 6px 18px rgba(0,0,0,0.12);
    overflow: hidden;
  }

  /* Decorative front */
  .card--front {
    background: var(--salmon); color: var(--card-white);
    display: flex; flex-direction: column; align-items: center; justify-content: center;
  }
  .front-mark {
    width: 170px; height: 170px; border-radius: 50%;
    border: 2px solid var(--card-white);
    display: flex; align-items: center; justify-content: center;
    margin-top: -20px;
  }
  .front-mark__name {
    font-size: 19px; font-weight: 600; letter-spacing: 3px; text-transform: uppercase;
    text-align: center; line-height: 1.3;
  }
  .front-url {
    position: absolute; bottom: 70px; left: 0; right: 0; text-align: center;
    font-size: 20px; letter-spacing: 6px;
  }

  /* Details back */
  .card--back { background: var(--card-white); }
  .back-logo {
    position: absolute; left: 70px; top: 34px; width: 190px;
    display: flex; flex-direction: column; align-items: center; gap: 10px;
  }
  .back-logo__ring {
    width: 92px; height: 92px; border-radius: 50%; border: 2px solid var(--mint);
  }
  .back-logo__name {
    color: var(--mint); font-size: 15px; font-weight: 600;
    letter-spacing: 4px; text-transform: uppercase;
  }
  .rule {
    position: absolute; left: 40px; right: 40px; height: 2px;
    background: linear-gradient(90deg, transparent, var(--rule) 15%, var(--rule) 85%, transparent);
  }
  .rule--top { top: 178px; }
  .rule--bottom { top: 350px; }
  .contact-list {
    position: absolute; left: 70px; top: 196px; list-style: none;
    font-size: 16px; color: var(--ink); line-height: 1.6;
  }
  .contact-list li { display: flex; align-items: center; gap: 10px; }
  .contact-list svg { width: 16px; height: 16px; flex: none; }
  .holder {
    position: absolute; right: 60px; top: 208px; text-align: right;
  }
  .holder__name { color: var(--mint); font-size: 24px; font-weight: 600; }
  .holder__title { color: var(--accent); font-size: 17px; margin-top: 4px; }
  .address {
    position: absolute; right: 60px; top: 288px; text-align: right;
    color: var(--ink); font-size: 17px; line-height: 1.3;
  }
</style>
</head>
<body>
<main class="sheet">
  <section class="card card--front" aria-label="Card front">
    <div class="front-mark">
      <span class="front-mark__name">Petal<br>Hollow</span>
    </div>
    <p class="front-url">www.petalhollow.com</p>
  </section>

  <section class="card card--back" aria-label="Card back">
    <div class="back-logo">
      <span class="back-logo__ring" aria-hidden="true"></span>
      <span class="back-logo__name">Petal Hollow</span>
    </div>
    <div class="rule rule--top"></div>

    <ul class="contact-list">
      <li>
        <svg viewBox="0 0 16 16" aria-hidden="true"><circle cx="8" cy="8" r="8" fill="var(--accent)"/><path d="M5 4.5l2 2-1 1c.6 1.2 1.3 1.9 2.5 2.5l1-1 2 2-1.2 1.2C7.6 12 4 8.4 3.8 5.7z" fill="#fff"/></svg>
        012-555-0142
      </li>
      <li>
        <svg viewBox="0 0 16 16" aria-hidden="true"><rect x="4" y="1" width="8" height="14" rx="1.5" fill="var(--accent)"/><rect x="5.5" y="3" width="5" height="8" fill="#fff"/></svg>
        012-555-0142
      </li>
      <li>
        <svg viewBox="0 0 16 16" aria-hidden="true"><rect x="1" y="3" width="14" height="10" rx="1.5" fill="var(--accent)"/><path d="M2 4.5l6 4.5 6-4.5" stroke="#fff" stroke-width="1.4" fill="none"/></svg>
        hello@petalhollow.com
      </li>
      <li>
        <svg viewBox="0 0 16 16" aria-hidden="true"><circle cx="8" cy="8" r="7" fill="var(--accent)"/><path d="M1.5 8h13M8 1c-2.5 3-2.5 11 0 14M8 1c2.5 3 2.5 11 0 14" stroke="#fff" stroke-width="1" fill="none"/></svg>
        www.petalhollow.com
      </li>
    </ul>

    <div class="holder">
      <p class="holder__name">Your Name</p>
      <p class="holder__title">Title</p>
    </div>
    <p class="address">Street Name, City Name<br>Zip Code-00000</p>
    <div class="rule rule--bottom"></div>
  </section>
</main>
</body>
</html>
```